Refresh of The Marston Collective business card

Update business card design using existing primary logo. Names, numbers, etc. are too hard to read on current design.

Target Market(s)

We are a CPA firm.

Industry/Entity Type

Accountant

Contact Information for Business Card

update current card

Colors
0355a3
3176b5
85acd3
0792cd

Requirements
Must have
• Easier to read phone numbers and names
• Use existing logo
Nice to have
• We love our color scheme and current TMC logo. But the names and phone numbers are too small and card just look old and stale.

```html
<!DOCTYPE html>
<html lang="en">
<head>
<meta charset="utf-8">
<title>The Marston Collective – Business Card</title>
<link href="https://fonts.googleapis.com/css2?family=Cinzel:wght@400;600&family=Lato:wght@400;700&display=swap" rel="stylesheet">
<style>
  :root {
    --navy: #0355a3;
    --mid-blue: #3176b5;
    --soft-blue: #85acd3;
    --bright-blue: #0792cd;
    --card-dark: #2b2c2e;
    --ink: #3a3a3a;
    --rule-grey: #555a60;
    --page: #eceef0;
    --white: #ffffff;
  }
  * { box-sizing: border-box; margin: 0; padding: 0; }
  html, body { width: 1200px; height: 800px; overflow: hidden; }
  body {
    background: var(--page);
    display: flex;
    align-items: center;
    justify-content: center;
    gap: 60px;
    font-family: "Lato", sans-serif;
  }
  .card {
    position: relative;
    width: 525px;
    height: 300px;
    border-radius: 18px;
    overflow: hidden;
    box-shadow: 0 8px 24px rgba(0,0,0,.18);
  }

  /* Back of card */
  .card--back {
    background: var(--card-dark);
    display: flex;
    flex-direction: column;
    align-items: center;
    justify-content: center;
    gap: 26px;
  }
  .brand {
    display: flex;
    align-items: center;
    gap: 18px;
  }
  .brand__dot {
    flex: none;
    border-radius: 50%;
    background: var(--mid-blue);
  }
  .brand__text { display: flex; flex-direction: column; }
  .brand__name {
    font-family: "Cinzel", serif;
    font-weight: 600;
    color: var(--mid-blue);
    letter-spacing: .04em;
    line-height: 1.1;
  }
  .brand__tagline {
    font-family: "Cinzel", serif;
    font-size: 8px;
    letter-spacing: .28em;
    text-transform: uppercase;
    margin-top: 6px;
    padding-top: 5px;
    border-top: 1px solid currentColor;
  }
  .card--back .brand__dot { width: 92px; height: 92px; }
  .card--back .brand__name { font-size: 30px; }
  .card--back .brand__tagline { color: #6d7075; }
  .website {
    font-size: 15px;
    color: var(--mid-blue);
    letter-spacing: .02em;
  }

  /* Front of card */
  .card--front { background: var(--white); }
  .card--front .brand {
    position: absolute;
    top: 26px;
    right: 28px;
    gap: 12px;
  }
  .card--front .brand__dot { width: 50px; height: 50px; }
  .card--front .brand__name { font-size: 18px; }
  .card--front .brand__tagline { color: #8a8d92; font-size: 6.5px; }

  .person {
    position: absolute;
    left: 0;
    top: 92px;
    padding-left: 34px;
    border-left: 14px solid var(--navy);
  }
  .person__name {
    font-family: "Cinzel", serif;
    font-size: 19px;
    color: var(--ink);
    letter-spacing: .03em;
  }
  .person__title {
    font-size: 15px;
    color: var(--mid-blue);
    margin-top: 2px;
  }
  .divider {
    position: absolute;
    left: 0;
    right: 0;
    top: 152px;
    height: 2px;
    background: linear-gradient(to right, var(--rule-grey) 0 56%, var(--navy) 56% 100%);
  }
  .contacts {
    position: absolute;
    left: 48px;
    top: 164px;
    list-style: none;
  }
  .contacts li {
    display: flex;
    align-items: center;
    gap: 12px;
    height: 22px;
    font-size: 14px;
    color: var(--ink);
  }
  .contacts svg { width: 18px; height: 18px; flex: none; }
  .address-band {
    position: absolute;
    left: 0; right: 0; bottom: 0;
    height: 40px;
    background: var(--navy);
    color: var(--white);
    font-size: 15px;
    display: flex;
    align-items: center;
    justify-content: flex-end;
    padding-right: 28px;
    letter-spacing: .01em;
  }
</style>
</head>
<body>

<section class="card card--back" aria-label="Card back">
  <div class="brand">
    <span class="brand__dot"></span>
    <div class="brand__text">
      <span class="brand__name">The Marston<br>Collective</span>
      <span class="brand__tagline">Certified Public Accountants</span>
    </div>
  </div>
  <p class="website">www.marstoncollective.com</p>
</section>

<section class="card card--front" aria-label="Card front">
  <div class="brand">
    <span class="brand__dot"></span>
    <div class="brand__text">
      <span class="brand__name">The Marston Collective</span>
      <span class="brand__tagline">Certified Public Accountants</span>
    </div>
  </div>

  <div class="person">
    <p class="person__name">DANIEL R. MARSTON, CPA</p>
    <p class="person__title">Job Title</p>
  </div>

  <div class="divider"></div>

  <ul class="contacts">
    <li>
      <svg viewBox="0 0 18 18" aria-hidden="true"><circle cx="9" cy="9" r="8.2" fill="none" stroke="var(--soft-blue)"/><path d="M6 5.5h2l.6 2-1.2.8a5 5 0 0 0 2.3 2.3l.8-1.2 2 .6v2a1 1 0 0 1-1 1A6.5 6.5 0 0 1 5 6.5a1 1 0 0 1 1-1z" fill="var(--navy)"/></svg>
      407.555.0142
    </li>
    <li>
      <svg viewBox="0 0 18 18" aria-hidden="true"><circle cx="9" cy="9" r="8.2" fill="none" stroke="var(--soft-blue)"/><rect x="6.5" y="4.5" width="5" height="9" rx="1" fill="var(--navy)"/><rect x="7.3" y="5.6" width="3.4" height="5.6" fill="#fff"/></svg>
      407.555.0187
    </li>
    <li>
      <svg viewBox="0 0 18 18" aria-hidden="true"><circle cx="9" cy="9" r="8.2" fill="none" stroke="var(--soft-blue)"/><rect x="5" y="8" width="8" height="5" rx="1" fill="var(--navy)"/><rect x="6.5" y="5" width="5" height="3.5" fill="var(--navy)"/></svg>
      407.555.0163
    </li>
    <li>
      <svg viewBox="0 0 18 18" aria-hidden="true"><circle cx="9" cy="9" r="8.2" fill="none" stroke="var(--soft-blue)"/><rect x="5" y="6" width="8" height="6" fill="var(--navy)"/><path d="M5 6l4 3.3L13 6" fill="none" stroke="#fff" stroke-width=".9"/></svg>
      dan@marstoncollective.com
    </li>
  </ul>

  <div class="address-band">812 Lakeview Ave. Suite 310, Winter Park, Florida 32789</div>
</section>

</body>
</html>
```